New singe page website for our software development company

We need a single webpage that includes information about our company, contact details and a job posting. It should scroll vertically with some cool animations and parallax scrolling effects.

We are a software development consulting company that writes custom software for our customers. The webpage should have graphics and illustrations that illustrate this.

Find our logo attached, it can be modified as needed.

Thanks for all the design. When looking through the various design it's clear to us, that car related images does not look right.

We got to have software design/engineering images instead.

Our unique selling points are:

• Custom software development
• Project Managment
• Industry Services
We want these displayed with some text and icons. The icons should either have the red/brown colour from our logo, or a colour that matches the design

Software

```html
<!DOCTYPE html>
<html lang="en">
<head>
<meta charset="utf-8">
<title>Kodevik</title>
<link href="https://fonts.googleapis.com/css2?family=Ubuntu:wght@400;500&family=Roboto:wght@400;500&display=swap" rel="stylesheet">
<style>
:root{
  --brown:#7b2a12;
  --brown-dark:#6e1f0c;
  --footer:#8e3c20;
  --blue:#1a7cc1;
  --green:#6dbd5c;
  --orange:#e86f47;
  --ink:#3a3a3a;
  --text:#666;
  --muted:#999;
  --line:#e6e6e6;
  --side:#f6f6f6;
}
*{margin:0;padding:0;box-sizing:border-box}
html,body{width:798px;height:1200px;overflow:hidden;background:#fff}
body{position:relative;font-family:"Roboto",Arial,sans-serif;color:var(--text)}
.abs{position:absolute}
.header{top:0;left:0;width:798px;height:48px;background:#fff;z-index:2;box-shadow:0 1px 3px rgba(0,0,0,.06)}
.brand{left:113px;top:14px;font-family:"Roboto",sans-serif;font-size:18px;color:var(--ink)}
.nav a{position:absolute;top:16px;font-family:"Ubuntu",sans-serif;font-size:11px;color:#444;text-decoration:none}
.nav a.active{color:var(--blue);border-bottom:1px solid var(--blue);padding-bottom:2px}
.search{border:1px solid #ddd;border-radius:2px;background:#fff;font-size:7.5px;color:#999;padding:0 8px;display:flex;align-items:center;justify-content:space-between}
.hero{top:48px;left:0;width:798px;height:331px;background:linear-gradient(100deg,#e9e4df 0%,#f4f1ee 35%,#f2efec 60%,#dcdcdc 100%)}
.hero-title{top:130px;width:798px;text-align:center;font-family:"Roboto",sans-serif;font-weight:400;font-size:50px;color:var(--ink);line-height:1}
.hero-sub{top:184px;width:798px;text-align:center;font-family:"Ubuntu",sans-serif;font-size:14.5px;color:var(--brown)}
.hero-rule{top:211px;left:240px;width:318px;height:1px;background:#c9a397}
.hero-text{top:221px;width:798px;text-align:center;font-size:11px;line-height:14px;color:var(--brown)}
.btn-read{top:261px;left:353px;width:92px;height:27px;background:#2a84cc;color:#fff;font-family:"Ubuntu",sans-serif;font-size:13px;font-weight:500;display:flex;align-items:center;justify-content:center}
.sidebar{top:379px;left:0;width:272px;height:525px;background:var(--side);border-right:1px solid #e2e2e2}
.h-brown{font-family:"Ubuntu",sans-serif;color:var(--brown)}
.brief-text{top:437px;left:114px;width:144px;font-size:8.4px;line-height:10.8px;color:#777;letter-spacing:-.1px}
.feedback{top:647px;left:114px;width:139px;height:78px;background:var(--brown-dark);color:#fff;padding:12px 12px}
.feedback p{font-size:8px;line-height:11px}
.feedback p small{font-size:7px}
.fb-btn{margin-top:6px;height:23px;background:#c0462a;display:flex;align-items:center;font-size:8.6px}
.fb-btn .ic{width:30px;height:23px;border-right:1px solid #a93a22;display:flex;align-items:center;justify-content:center}
.fb-btn span{flex:1;text-align:center}
.t-text{top:774px;left:114px;width:144px;font-size:8.6px;line-height:11.4px;color:#777}
.avatar{top:838px;left:222px;width:30px;height:30px;border-radius:50%;background:#6b5a4e}
.jobs-title{top:408px;left:298px;font-family:"Ubuntu",sans-serif;font-size:18px;color:var(--blue)}
.jobs-sub{top:434px;left:299px;font-size:9px;color:var(--brown)}
.job{left:298px;width:386px;height:53px;border-top:1px solid var(--line)}
.job.feat{left:272px;width:412px;padding-left:26px;background:#eef6fd}
.job .t{position:absolute;top:15px;font-size:9.5px;color:#555}
.job .c{position:absolute;top:29px;font-size:8px;color:var(--blue);letter-spacing:.2px}
.job .loc,.job .dt{position:absolute;top:21px;font-size:8px;color:#aaa}
.job .loc{left:219px}.job .dt{left:279px}
.job.feat .loc{left:245px}.job.feat .dt{left:305px}
.job .apply{position:absolute;right:0;top:16px;width:63px;height:16px;background:var(--green);color:#fff;font-size:9px;display:flex;align-items:center;justify-content:center}
.job .apply.hot{background:var(--orange)}
.job .star{position:absolute;left:9px;top:20px;font-size:9px;color:#bbb}
.load{top:838px;left:272px;width:412px;height:31px;background:#efe4e0;color:var(--brown);font-size:11px;display:flex;align-items:center;justify-content:center}
.map{top:904px;left:0;width:798px;height:174px;background:linear-gradient(135deg,#e8e4da 0%,#e2e6d4 45%,#cfe3c0 75%,#dfe4d8 100%);border-top:1px solid #ccc}
.bar{top:1078px;left:0;width:798px;height:30px;background:#fff}
.phone{left:126px;top:1086px;font-family:"Ubuntu",sans-serif;font-size:12px;color:var(--blue);display:flex;align-items:center;gap:6px}
.or{left:226px;top:1085px;width:16px;height:16px;border-radius:50%;background:var(--blue);color:#fff;font-size:7px;display:flex;align-items:center;justify-content:center}
.footer{top:1108px;left:0;width:798px;height:92px;background:var(--footer)}
.fbox{height:24px;border:1px solid #d9a48f;color:#fff;font-family:"Ubuntu",sans-serif;font-size:11.5px;display:flex;align-items:center;padding-left:10px;gap:10px}
.fbox.top{background:#fff;color:var(--blue);border-color:#fff;justify-content:space-between;padding:0 10px 0 13px}
.fbox.copy{justify-content:center;padding:0}
</style>
</head>
<body>
<header class="abs header">
  <div class="abs brand">Kodevik</div>
  <nav class="nav">
    <a class="active" style="left:330px">About Us</a>
    <a style="left:395px">Contact details</a>
    <a style="left:486px">Job posting</a>
  </nav>
  <div class="abs search" style="left:569px;top:14px;width:115px;height:21px">Search
    <svg width="10" height="10" viewBox="0 0 10 10"><circle cx="4" cy="4" r="3" fill="none" stroke="#bbb" stroke-width="1.2"/><line x1="6.3" y1="6.3" x2="9" y2="9" stroke="#bbb" stroke-width="1.2"/></svg></div>
</header>

<section class="abs hero" role="img" aria-label="Faded photo of a software team meeting with a presenter at a whiteboard"></section>
<svg class="abs" style="left:656px;top:62px" width="18" height="18" viewBox="0 0 18 18"><path d="M9 2a7 7 0 1 1-6.5 4.4" fill="none" stroke="#2a84cc" stroke-width="1.6"/></svg>
<h1 class="abs hero-title">Kodevik</h1>
<div class="abs hero-sub">Software Development Consulting</div>
<div class="abs hero-rule"></div>
<p class="abs hero-text">Lorem Ipsum is that it has a more-or-less normal distribution<br>of letters, as opposed to using 'Content here,</p>
<div class="abs btn-read">Read More</div>

<aside class="abs sidebar"></aside>
<h2 class="abs h-brown" style="top:409px;left:114px;font-size:16px;font-weight:400">Brief</h2>
<p class="abs brief-text">There are many variations of pas-sages of Lorem Ipsum available, but the majority have suffered alteration in some form, by injected humour, or randomised words which don't look even slightly believable. If you are going to use a passage of Lorem Ipsum, you need to be sure there isn't anything embarrassing hidden in the middle of text. All the Lorem Ipsum generators on the Internet tend to repeat predefined chunks as necessary, making this the first true generator on the Inter-net. It uses a dictionary of over 200 Latin words,</p>
<div class="abs feedback">
  <p>Please help us to improve we<br><small>read each and every suggetion</small></p>
  <div class="fb-btn"><div class="ic"><svg width="11" height="9" viewBox="0 0 11 9"><path d="M1 3h2l5-2v7L3 6H1z" fill="none" stroke="#f3c1b3" stroke-width="1"/></svg></div><span>Send Feedback</span></div>
</div>
<div class="abs" style="top:743px;left:114px;width:139px;height:1px;background:#e6e6e6"></div>
<h3 class="abs h-brown" style="top:755px;left:114px;font-size:11.5px;font-weight:400">Testimonials</h3>
<p class="abs t-text">Working with KLS Software was easy and convenient. Jonas was very helpful and patient in making sure the database was exactly what we needed..</p>
<div class="abs" style="top:843px;left:130px;width:75px;text-align:right;font-size:8px;color:var(--brown)">Carla Vinter<br><span style="color:#999;font-size:6.8px;display:block;margin-top:-2px">Sr. Manager</span></div>
<div class="abs" style="top:836px;left:214px;width:1px;height:28px;background:#ddd"></div>
<div class="abs avatar" role="img" aria-label="Portrait of the reviewer"></div>

<h2 class="abs jobs-title" style="font-weight:400">Showing: All Jobs</h2>
<p class="abs jobs-sub">You are viewing All Types of Jobs from All States - All Countries</p>

<div class="abs job" style="top:463px"><div class="t">Entry level opnings for Business</div><div class="c">Required at Northwell Inc</div><div class="loc">⚲ Lindvei</div><div class="dt">◦ 21 fab</div><div class="apply">Apply Now</div></div>
<div class="abs job" style="top:516px"><div class="t">Full time Content Writer</div><div class="c">Required at Inkfield</div><div class="loc">⚲ Lindvei</div><div class="dt">◦ 21 fab</div><div class="apply">Apply Now</div></div>
<div class="abs job feat" style="top:569px"><div class="star">★</div><div class="t">Social Media Expert</div><div class="c">Required at Brevio</div><div class="loc">⚲ Lindvei</div><div class="dt">◦ 21 fab</div><div class="apply hot">Apply Now</div></div>
<div class="abs job" style="top:621px"><div class="t">Opening for PHP Developer/Web</div><div class="c">Required at Lumen Studio</div><div class="loc">⚲ Lindvei</div><div class="dt">◦ 21 fab</div><div class="apply">Apply Now</div></div>
<div class="abs job" style="top:674px;height:55px"><div class="t" style="top:19px">Entry level opnings for Business</div><div class="c" style="top:33px">Required at Northwell Inc</div><div class="loc" style="top:25px">⚲ Lindvei</div><div class="dt" style="top:25px">◦ 21 fab</div><div class="apply" style="top:21px">Apply Now</div></div>
<div class="abs job" style="top:729px"><div class="t">Social Media Expert</div><div class="c">Required at Brevio</div><div class="loc">⚲ Lindvei</div><div class="dt">◦ 21 fab</div><div class="apply">Apply Now</div></div>
<div class="abs job" style="top:782px;height:56px"><div class="t" style="top:17px">Opening for PHP Developer/Web</div><div class="c" style="top:31px">Required at Lumen Studio</div><div class="loc" style="top:24px">⚲ Lindvei</div><div class="dt" style="top:24px">◦ 21 fab</div><div class="apply" style="top:19px">Apply Now</div></div>
<div class="abs load">Load Next 35 Jobs</div>

<div class="abs map" role="img" aria-label="Street map of the office neighbourhood with a location marker and a support agent illustration"></div>

<div class="abs bar"></div>
<div class="abs phone"><svg width="11" height="11" viewBox="0 0 11 11"><path d="M2 1l2 2-1 1.5c.8 1.6 2 2.8 3.5 3.5L8 7l2 2-1.5 1.5C5 10 1 6 .5 2.5z" fill="#1a7cc1"/></svg>40-18-62-00</div>
<div class="abs or">or</div>
<div class="abs search" style="left:259px;top:1085px;width:116px;height:18px">Search
  <svg width="10" height="10" viewBox="0 0 10 10"><circle cx="4" cy="4" r="3" fill="none" stroke="#bbb" stroke-width="1.2"/><line x1="6.3" y1="6.3" x2="9" y2="9" stroke="#bbb" stroke-width="1.2"/></svg></div>

<footer class="abs footer"></footer>
<div class="abs fbox" style="top:1125px;left:114px;width:262px"><svg width="10" height="13" viewBox="0 0 10 13"><path d="M5 12C2 8 1 6 1 4.5a4 4 0 0 1 8 0C9 6 8 8 5 12z" fill="#fff"/><circle cx="5" cy="4.5" r="1.5" fill="#8e3c20"/></svg>Lindvei 12b0380 Nordby</div>
<div class="abs fbox top" style="top:1125px;left:422px;width:262px">Back top the top<svg width="10" height="7" viewBox="0 0 10 7"><path d="M1 6l4-4 4 4" fill="none" stroke="#1a7cc1" stroke-width="2"/></svg></div>
<div class="abs fbox" style="top:1160px;left:114px;width:262px"><svg width="14" height="10" viewBox="0 0 14 10"><rect x=".5" y=".5" width="13" height="9" fill="#fff"/><path d="M.5 .5L7 5.5 13.5 .5" fill="none" stroke="#8e3c20"/></svg>post@kodevik.no</div>
<div class="abs fbox copy" style="top:1160px;left:422px;width:262px">© Copyright 2014 kodevik.no</div>
</body>
</html>
```